copper ridge construction website (squarespace build)

construction website - see attached documents

Target Market(s)

owners, cm's, and gc's

Coding

Coded - Design and coding required

Font styles to use
Serif

Colors
0054AA
0677BA
7BADD7
CADEEF
E8F1F8

```html
<!DOCTYPE html>
<html lang="en">
<head>
<meta charset="utf-8">
<title>Copper Ridge Construction</title>
<link href="https://fonts.googleapis.com/css2?family=Montserrat:wght@400;500;600;700;800&display=swap" rel="stylesheet">
<style>
:root{
  --navy:#0c2b5e;
  --navy-deep:#0a2452;
  --ink:#1f2a3a;
  --text:#3a3f48;
  --muted:#5b6270;
  --white:#ffffff;
  --about-grey:#626262;
  --band-grey:#e6e6e6;
  --footer-bar:#3d4b66;
  --sky-top:#c9d6e4;
  --sky-low:#e7edf3;
  --soil:#b9a183;
}
*{margin:0;padding:0;box-sizing:border-box}
html,body{width:1200px;height:3597px;overflow:hidden;background:var(--white)}
body{font-family:"Montserrat",Arial,sans-serif;color:var(--text);position:relative}
.abs{position:absolute}
a{color:inherit;text-decoration:none}

/* header */
.site-header{position:absolute;left:0;top:0;width:1200px;height:85px;background:var(--white)}
.brand{position:absolute;left:112px;top:24px;width:208px;height:36px;border:2px solid var(--navy);display:flex;align-items:center;justify-content:center;font-weight:700;font-size:20px;color:var(--navy);letter-spacing:1px}
.main-nav{position:absolute;top:32px;font-size:15px;color:var(--ink)}
.main-nav.active{font-weight:700;color:var(--navy)}
.btn{position:absolute;display:flex;align-items:center;background:var(--navy);color:var(--white);font-size:14px;font-weight:500;padding-left:11px}
.btn .btn-icon{position:absolute;right:3px;top:3px;bottom:3px;width:36px;background:var(--white);display:flex;align-items:center;justify-content:center}
.btn-icon svg{width:16px;height:12px}

/* hero */
.hero{position:absolute;left:0;top:85px;width:1200px;height:558px;background:linear-gradient(180deg,var(--sky-top) 0%,var(--sky-low) 70%,var(--soil) 88%,#9d8466 100%)}
.hero-rig{position:absolute;left:660px;top:0;width:540px;height:520px;background:linear-gradient(160deg,rgba(90,90,90,.35),rgba(226,180,40,.55) 60%,rgba(80,70,50,.4));}
.hero-kicker{position:absolute;left:110px;top:166px;font-size:44px;font-weight:400;color:#4a4f58;letter-spacing:1px}
.hero-title{position:absolute;left:110px;top:214px;font-size:43px;font-weight:800;color:var(--navy);line-height:52px;letter-spacing:.5px}
.rule{position:absolute;height:4px}
.rule .thin{position:absolute;left:0;top:1px;height:1px;background:var(--navy);width:100%}
.rule .thick{position:absolute;top:0;height:4px;background:var(--navy)}
.hero-copy{position:absolute;left:112px;top:368px;width:470px;font-size:17.5px;line-height:26px;color:var(--ink)}

/* section headings */
.section-title{position:absolute;left:0;width:1200px;text-align:center;font-size:34px;color:var(--ink);font-weight:400}
.section-title b{font-weight:700;color:var(--navy)}

/* service cards */
.card{position:absolute;top:840px;width:468px;height:315px;box-shadow:0 2px 10px rgba(0,0,0,.15)}
.card-light{left:112px;background:var(--white)}
.card-dark{left:619px;background:var(--navy)}
.card .photo{position:absolute;left:17px;top:25px;width:208px;height:264px}
.card-dark .photo{border:2px solid var(--white)}
.card h3{position:absolute;left:244px;top:26px;font-size:18.5px;font-weight:500;line-height:23px;color:var(--ink)}
.card-dark h3{color:var(--white)}
.card ul{position:absolute;left:244px;top:84px;width:215px;list-style:none}
.card li{position:relative;padding-left:23px;font-size:12.5px;line-height:15px;margin-bottom:10px;color:var(--muted)}
.card-dark li{color:var(--white);margin-bottom:10px}
.card li::before{content:"»";position:absolute;left:2px;top:-3px;font-size:16px;color:var(--navy)}
.card-dark li::before{color:var(--white)}
.more{position:absolute;left:244px;top:273px;font-size:14px;font-weight:500;color:var(--navy)}
.card-dark .more{color:var(--white)}
.circle-arrow{position:absolute;width:48px;height:48px;border-radius:50%;display:flex;align-items:center;justify-content:center}
.circle-arrow.solid{background:var(--navy)}
.circle-arrow.outline{border:2px solid var(--navy);background:var(--white)}
.circle-arrow svg{width:14px;height:18px}

/* about */
.grey-band{position:absolute;left:0;top:1555px;width:1200px;height:915px;background:var(--band-grey)}
.about-panel{position:absolute;left:61px;top:1243px;width:1079px;height:492px;background:var(--about-grey)}
.about-kicker{position:absolute;left:115px;top:1325px;font-size:34px;color:var(--white);font-weight:400}
.about-title{position:absolute;left:115px;top:1366px;font-size:34px;font-weight:700;color:var(--white)}
.about-copy{position:absolute;left:113px;top:1459px;width:465px;font-size:14.5px;line-height:23px;color:var(--white)}
.about-copy p+p{margin-top:23px}
.about-frame{position:absolute;left:666px;top:1327px;width:421px;height:322px;border:2px solid var(--white)}
.about-photo{position:absolute;left:686px;top:1347px;width:381px;height:248px;background:linear-gradient(135deg,#4c6a9e,#8aa0c2 45%,#c9b8a4 80%,#7b7b7b)}
.expert-card{position:absolute;left:847px;top:1503px;width:220px;height:116px;background:var(--white);padding:20px 20px}
.expert-card h4{font-size:12.5px;font-weight:600;color:var(--navy);text-decoration:underline}
.expert-card p{margin-top:8px;font-size:9.5px;line-height:14px;color:var(--muted)}

/* markets */
.rig-drawing{position:absolute;left:0;top:1781px;width:363px;height:356px;background:radial-gradient(ellipse at 40% 60%,rgba(120,140,170,.22),rgba(230,230,230,0) 70%)}
.markets-intro{position:absolute;left:240px;top:1911px;width:720px;text-align:center;font-size:15px;line-height:26px;color:var(--text)}
.market{position:absolute;width:290px}
.market .icon{width:84px;height:84px;background:var(--navy);display:flex;align-items:center;justify-content:center}
.market .icon svg{width:46px;height:46px}
.market h4{margin-top:21px;font-size:17.5px;font-weight:500;color:var(--ink)}
.market p{margin-top:6px;font-size:13.5px;line-height:17px;color:var(--muted)}

/* projects */
.projects-kicker{position:absolute;left:112px;top:2551px;font-size:34px;color:var(--ink)}
.projects-title{position:absolute;left:112px;top:2592px;font-size:34px;font-weight:700;color:var(--navy)}
.project{position:absolute;top:2710px;width:304px}
.project .shot{height:333px}
.project .label{position:relative;margin:7px 1px 0;height:33px;background:var(--navy);color:var(--white);font-size:14px;font-weight:600;display:flex;align-items:center;padding-left:10px}
.project .label .btn-icon{position:absolute;right:3px;top:3px;bottom:3px;width:40px;background:var(--white);display:flex;align-items:center;justify-content:center}

/* footer */
.site-footer{position:absolute;left:0;top:3252px;width:1200px;height:296px;background:var(--navy-deep)}
.footer-brand{position:absolute;left:112px;top:3322px;font-size:28px;font-weight:700;color:var(--white);line-height:30px;letter-spacing:1px}
.footer-about{position:absolute;left:112px;top:3396px;width:250px;font-size:15px;line-height:23px;color:var(--white)}
.footer-col{position:absolute;top:3306px;color:var(--white)}
.footer-col h5{font-size:19.5px;font-weight:600;letter-spacing:.3px}
.footer-col .col-rule{position:relative;margin-top:14px;width:130px;height:3px}
.footer-col .col-rule::before{content:"";position:absolute;left:0;top:1px;width:100%;height:1px;background:rgba(255,255,255,.7)}
.footer-col .col-rule::after{content:"";position:absolute;left:0;top:0;width:40px;height:3px;background:var(--white)}
.footer-col ul{list-style:none;margin-top:21px}
.footer-col li{font-size:15px;line-height:25px}
.footer-bar{position:absolute;left:0;top:3548px;width:1200px;height:49px;background:var(--footer-bar);color:#e4e8ef;font-size:13px;display:flex;align-items:center;justify-content:center}
</style>
</head>
<body>

<header class="site-header">
  <div class="brand">COPPER RIDGE</div>
  <nav>
    <a class="main-nav active" style="left:461px">HOME</a>
    <a class="main-nav" style="left:539px">ABOUT</a>
    <a class="main-nav" style="left:624px">SERVICES</a>
    <a class="main-nav" style="left:729px">PROJECT</a>
    <a class="main-nav" style="left:830px">MARKET</a>
  </nav>
  <a class="btn" style="left:928px;top:25px;width:160px;height:35px">CONTACT US
    <span class="btn-icon"><svg viewBox="0 0 16 12"><path d="M2 1l5 5-5 5M8 1l5 5-5 5" fill="none" stroke="#0c2b5e" stroke-width="2.2"/></svg></span></a>
</header>

<section class="hero">
  <div class="hero-rig" role="img" aria-label="Yellow foundation drilling rig on a construction site under a cloudy sky"></div>
</section>
<div class="hero-kicker">BUILDING</div>
<h1 class="hero-title">EXCELLENCE THROUGH<br>EXPERIENCE.</h1>
<div class="rule" style="left:112px;top:333px;width:188px"><span class="thin"></span><span class="thick" style="left:0;width:63px"></span></div>
<p class="hero-copy">Copper Ridge Construction is a self-performing foundation and geotechnical general contractor &amp; the critical first phase of every successful project.</p>
<a class="btn" style="left:112px;top:465px;width:184px;height:33px">VIEW PROJECTS
  <span class="btn-icon"><svg viewBox="0 0 16 12"><path d="M2 1l5 5-5 5M8 1l5 5-5 5" fill="none" stroke="#0c2b5e" stroke-width="2.2"/></svg></span></a>

<h2 class="section-title" style="top:720px">OUR <b>SERVICES</b></h2>
<div class="rule" style="left:506px;top:783px;width:188px"><span class="thin"></span><span class="thick" style="left:64px;width:61px"></span></div>

<div class="circle-arrow solid" style="left:37px;top:973px"><svg viewBox="0 0 14 18"><path d="M10 2L3 9l7 7" fill="none" stroke="#fff" stroke-width="2.4"/></svg></div>
<div class="circle-arrow outline" style="left:1116px;top:973px"><svg viewBox="0 0 14 18"><path d="M4 2l7 7-7 7" fill="none" stroke="#0c2b5e" stroke-width="2.4"/></svg></div>

<article class="card card-light">
  <div class="photo" role="img" aria-label="Drilling rig working on an urban foundation site" style="background:linear-gradient(160deg,#6f8a5a,#7a5a44 50%,#9a9a9a)"></div>
  <h3>Owner, CM's, &amp;<br>GC's Services</h3>
  <ul>
    <li>Complete turnkey site &amp; structural packages</li>
    <li>Site constructability and logistical assessments</li>
    <li>Value engineering</li>
    <li>Geotechnical &amp; foundation engineering</li>
    <li>Geotechnical review &amp; design support</li>
  </ul>
  <a class="more">MORE DETAILS ↗</a>
</article>
<article class="card card-dark">
  <div class="photo" role="img" aria-label="Timber-lagged excavation pit with soil floor" style="background:linear-gradient(180deg,#a98c64,#8d6f4c 55%,#7a6650)"></div>
  <h3>Engineering &amp;<br>Design Support</h3>
  <ul>
    <li>Design review and support</li>
    <li>Structural monitoring</li>
    <li>Engineering &amp; design</li>
    <li>Preconstruction services</li>
    <li>Exploratory investigations</li>
    <li>Design proof testing</li>
  </ul>
  <a class="more">MORE DETAILS ↗</a>
</article>

<div class="grey-band"></div>
<section class="about-panel"></section>
<div class="about-kicker">ABOUT</div>
<h2 class="about-title">COPPER RIDGE</h2>
<div class="rule" style="left:114px;top:1424px;width:188px"><span class="thin" style="background:#fff"></span><span class="thick" style="left:0;width:63px;background:#fff"></span></div>
<div class="about-copy">
  <p>Copper Ridge Construction is a self-performing foundation and geotechnical general contractor &amp; the critical first phase of every successful project.</p>
  <p>Copper Ridge partners with owners, construction managers, and general contractors from design through construction</p>
</div>
<a class="btn" style="left:113px;top:1615px;width:154px;height:33px;border:2px solid #fff">READ MORE
  <span class="btn-icon"><svg viewBox="0 0 16 12"><path d="M2 1l5 5-5 5M8 1l5 5-5 5" fill="none" stroke="#0c2b5e" stroke-width="2.2"/></svg></span></a>
<div class="about-frame"></div>
<div class="about-photo" role="img" aria-label="Crew inspecting rows of blue steel shoring braces"></div>
<div class="expert-card">
  <h4>CONTACT OUR EXPERTS</h4>
  <p>Our projects managed and built by experienced professionals and skilled craftsmen.</p>
</div>

<div class="rig-drawing" role="img" aria-label="Line drawing of a tracked drilling rig"></div>
<h2 class="section-title" style="top:1810px">MARKETS <b>WE SERVE</b></h2>
<div class="rule" style="left:506px;top:1873px;width:188px"><span class="thin"></span><span class="thick" style="left:64px;width:61px"></span></div>
<p class="markets-intro">Copper Ridge Construction serves owners, construction managers, and general contractors and subcontractors across the New York, New Jersey, and Connecticut tri-state region.</p>

<div class="market" style="left:450px;top:1999px">
  <div class="icon"><svg viewBox="0 0 46 46" fill="none" stroke="#fff" stroke-width="1.5"><rect x="14" y="6" width="18" height="34"/><path d="M18 11h3M25 11h3M18 17h3M25 17h3M18 23h3M25 23h3M18 29h3M25 29h3M21 40v-6h4v6M8 40h30"/></svg></div>
  <h4>Commercial</h4>
  <p>Office, retail, and mixed-use foundation and structural packages</p>
</div>
<div class="market" style="left:789px;top:1999px">
  <div class="icon"><svg viewBox="0 0 46 46" fill="none" stroke="#fff" stroke-width="1.5"><path d="M6 40V18h12M18 40V10h22v30M4 40h38M22 15h4M30 15h4M22 21h4M30 21h4M22 27h4M30 27h4M9 24h5M9 30h5M27 40v-6h4v6"/></svg></div>
  <h4>Residential</h4>
  <p>Multi-family and single-family foundation, underpinning, and earth-retention work</p>
</div>
<div class="market" style="left:112px;top:2216px">
  <div class="icon"><svg viewBox="0 0 46 46" fill="none" stroke="#fff" stroke-width="1.5"><path d="M5 40V24l8-5v5l8-5v5l8-5v5h6V8h4v32zM4 40h38M10 31h3v3h-3zM17 31h3v3h-3zM24 31h3v3h-3zM35 4c2 0 3 1 4 2"/></svg></div>
  <h4>Industrial</h4>
  <p>Warehouse and distribution center foundation systems, including complete</p>
</div>
<div class="market" style="left:450px;top:2216px">
  <div class="icon"><svg viewBox="0 0 46 46" fill="none" stroke="#fff" stroke-width="1.5"><circle cx="23" cy="23" r="15"/><rect x="16" y="13" width="14" height="20"/><path d="M19 17h3M24 17h3M19 22h3M24 22h3M19 27h3M24 27h3"/></svg></div>
  <h4>Public Works &amp; Infrastructure</h4>
  <p>Municipal, transportation, and public agency projects</p>
</div>
<div class="market" style="left:789px;top:2216px">
  <div class="icon"><svg viewBox="0 0 46 46" fill="none" stroke="#fff" stroke-width="1.5"><path d="M6 40V20h8V10h18v10h8v20M4 40h38M20 14h6M23 11v6M18 22h3M25 22h3M18 28h3M25 28h3M9 25h3M9 31h3M34 25h3M34 31h3M21 40v-6h4v6"/></svg></div>
  <h4>Institutional</h4>
  <p>Healthcare, education, and government facility foundation work</p>
</div>

<div class="projects-kicker">OUR</div>
<h2 class="projects-title">PROJECT EXCELLENCE</h2>
<div class="rule" style="left:112px;top:2650px;width:188px"><span class="thin"></span><span class="thick" style="left:0;width:63px"></span></div>

<article class="project" style="left:112px">
  <div class="shot" role="img" aria-label="Concrete mid-rise building under construction with scaffolding and crane" style="background:linear-gradient(180deg,#4f86c6,#9cbbd9 45%,#b9b2a4 75%,#8a7d68)"></div>
  <div class="label">HUDSON RIVER COMMERCIAL<span class="btn-icon"><svg viewBox="0 0 16 12" width="16" height="12"><path d="M2 1l5 5-5 5M8 1l5 5-5 5" fill="none" stroke="#0c2b5e" stroke-width="2.2"/></svg></span></div>
</article>
<article class="project" style="left:448px">
  <div class="shot" role="img" aria-label="Workers on a concrete deck with tower cranes under blue sky" style="background:linear-gradient(180deg,#3f7fd0,#86b3e4 40%,#a59a84 70%,#6f6a5e)"></div>
  <div class="label">CROSSPOINT LOGISTICS<span class="btn-icon"><svg viewBox="0 0 16 12" width="16" height="12"><path d="M2 1l5 5-5 5M8 1l5 5-5 5" fill="none" stroke="#0c2b5e" stroke-width="2.2"/></svg></span></div>
</article>
<article class="project" style="left:785px">
  <div class="shot" role="img" aria-label="Aerial view of concrete high-rise frames with a yellow crane" style="background:linear-gradient(160deg,#6d6d6d,#9a9a9a 40%,#b89a3a 60%,#555)"></div>
  <div class="label">RIVERSIDE RESIDENCES<span class="btn-icon"><svg viewBox="0 0 16 12" width="16" height="12"><path d="M2 1l5 5-5 5M8 1l5 5-5 5" fill="none" stroke="#0c2b5e" stroke-width="2.2"/></svg></span></div>
</article>

<div class="circle-arrow solid" style="left:542px;top:3119px"><svg viewBox="0 0 14 18"><path d="M10 2L3 9l7 7" fill="none" stroke="#fff" stroke-width="2.4"/></svg></div>
<div class="circle-arrow outline" style="left:610px;top:3119px"><svg viewBox="0 0 14 18"><path d="M4 2l7 7-7 7" fill="none" stroke="#0c2b5e" stroke-width="2.4"/></svg></div>

<footer class="site-footer"></footer>
<div class="footer-brand">COPPER<br>RIDGE</div>
<p class="footer-about">Copper Ridge Construction is a self-performing foundation &amp; geotechnical general contractor</p>
<div class="footer-col" style="left:414px">
  <h5>QUICK LINKS</h5><div class="col-rule"></div>
  <ul><li>Home</li><li>About Us</li><li>Our Services</li><li>Project Porfilio</li><li>Market</li><li>Contact</li></ul>
</div>
<div class="footer-col" style="left:606px">
  <h5>SERVICES</h5><div class="col-rule"></div>
  <ul><li>Owner, CM's, and GC's Services</li><li>Foundation &amp; Earth Retention</li><li>Reinforced Concrete, Masonry, &amp; Other</li><li>Engineering &amp; Design Support</li></ul>
</div>
<div class="footer-col" style="left:949px">
  <h5>OTHER LINKS</h5><div class="col-rule"></div>
  <ul><li>Help Center</li><li>Terms &amp; Conditions</li><li>Privacy Policy</li><li>Sitemaps</li></ul>
</div>
<div class="footer-bar">© 2026 Copper Ridge. All rights reserved.</div>

</body>
</html>
```